We need motivational posters designed to be used in classrooms at a truck driving school. The purpose of the posters is to motivate the students.

I want the the quotes to be the main focal point of emphasis and our logo on the bottom of the poster for branding purposes.

I would like the images to be related to the trucking industry

Below are the quotes for the posters

Poster 1
"Start where you are. Use what you have. Do what you can."
-Delmar Quisby-

Poster 2
"The secret of getting ahead is getting started"
-Owen Farrow-

Poster 3
"Most effective way to do it, is to do it."
-Rosalind Pemberly-

Poster 4
"Set your goals big, and don't stop till you get there."
-Cy Whitlock-

Poster 5
"If you are not willing to learn, no one can help you. If you are determined to learn, no one can stop you."
-Unknown-

Poster 6
"The will to succeed is important, but what's more important is the will to prepare."
-Dougie Hallam-

THESE POSTERS SHOULD BE DESIGNED AS 18X24
LANDSCAPE AND PORTRAIT ORIENTATION

Industry/Entity Type

School

```html
<!DOCTYPE html>
<html lang="en">
<head>
<meta charset="utf-8">
<title>The Secret of Getting Ahead – Classroom Poster</title>
<link href="https://fonts.googleapis.com/css2?family=Ultra&family=Yellowtail&family=Oswald:wght@500&display=swap" rel="stylesheet">
<style>
  :root {
    --ink: #111111;
    --gold: #fbb919;
    --paper: #ffffff;
  }
  html, body {
    margin: 0;
    padding: 0;
    width: 935px;
    height: 1200px;
    overflow: hidden;
    background: var(--paper);
  }
  .poster {
    position: relative;
    width: 935px;
    height: 1200px;
    background: var(--paper);
  }
  .poster-frame {
    position: absolute;
    inset: 0;
  }
  .quote {
    position: absolute;
    inset: 0;
  }
  .quote .block {
    font-family: "Ultra", serif;
    fill: var(--ink);
  }
  .quote .script {
    font-family: "Yellowtail", cursive;
    fill: var(--gold);
  }
  .attribution {
    position: absolute;
    left: 560px;
    top: 948px;
    margin: 0;
    font-family: "Oswald", sans-serif;
    font-weight: 500;
    font-size: 36px;
    letter-spacing: 1px;
    color: var(--ink);
    text-transform: uppercase;
  }
  .ignition-art {
    position: absolute;
    left: 127px;
    top: 882px;
    width: 204px;
    height: 204px;
    background: var(--ink);
    border-radius: 0 100% 0 0;
  }
  .key-art {
    position: absolute;
    left: 365px;
    top: 988px;
    width: 195px;
    height: 80px;
    background: var(--gold);
    border-radius: 40px 8px 8px 40px;
  }
  .school-mark {
    position: absolute;
    left: 612px;
    top: 1018px;
    display: flex;
    align-items: center;
    gap: 10px;
    font-family: "Oswald", sans-serif;
    font-weight: 500;
    font-size: 19px;
    line-height: 1.05;
    color: var(--ink);
    text-transform: uppercase;
  }
  .school-mark .dot {
    width: 44px;
    height: 44px;
    border-radius: 50%;
    background: var(--gold);
    flex: none;
  }
</style>
</head>
<body>
<main class="poster">
  <svg class="poster-frame" width="935" height="1200" viewBox="0 0 935 1200" aria-hidden="true">
    <rect x="92" y="89" width="753" height="1036" fill="none" stroke="var(--ink)" stroke-width="14"/>
    <rect x="105" y="104" width="727" height="1006" fill="none" stroke="var(--gold)" stroke-width="6"/>
  </svg>

  <svg class="quote" width="935" height="1200" viewBox="0 0 935 1200" role="img" aria-label="The secret of getting ahead is getting started.">
    <text class="block" x="160" y="210" font-size="80" textLength="188" lengthAdjust="spacingAndGlyphs">THE</text>
    <text class="script" x="318" y="300" font-size="175" textLength="345" lengthAdjust="spacingAndGlyphs">secret</text>
    <text class="block" x="156" y="448" font-size="96" textLength="574" lengthAdjust="spacingAndGlyphs">OF GETTING</text>
    <text class="block" x="156" y="594" font-size="138" textLength="574" lengthAdjust="spacingAndGlyphs">AHEAD</text>
    <text class="block" x="156" y="710" font-size="96" textLength="574" lengthAdjust="spacingAndGlyphs">IS GETTING</text>
    <text class="script" x="252" y="880" font-size="190" textLength="530" lengthAdjust="spacingAndGlyphs">started.</text>
  </svg>

  <p class="attribution">-Owen Farrow</p>

  <div class="ignition-art" role="img" aria-label="Ignition switch with key positions off, acc, on, start"></div>
  <div class="key-art" role="img" aria-label="Truck ignition key"></div>

  <div class="school-mark">
    <span class="dot"></span>
    <span>Ironline Truck<br>Driving School</span>
  </div>
</main>
</body>
</html>
```